Business card

A basic business card using the new logo
The logo has our address on it is all I need is onset with the following

Dale Whitford
Manager of Sales and Service

Cell 508-731-2286

Email dw71846@mailbrook.net

Next card

Neil Ostrand
Manager

Cell 978-215-3907

Email nostrand7@qx.net

```html
<!DOCTYPE html>
<html lang="en">
<head>
<meta charset="utf-8">
<title>NTS Business Card</title>
<link rel="stylesheet" href="https://fonts.googleapis.com/css2?family=Arimo:wght@400;500;700&family=Exo+2:ital,wght@1,800&display=swap">
<style>
  :root {
    --backdrop: #d9dbde;
    --card-white: #f4f5f6;
    --brand-blue: #2f86c7;
    --brand-blue-light: #4aa6e4;
    --brand-blue-deep: #1f6aa5;
    --tab-blue: #9cc3e2;
    --ink: #1c1c1c;
  }
  * { box-sizing: border-box; margin: 0; padding: 0; }
  html, body { width: 1200px; height: 900px; overflow: hidden; }
  body {
    background: var(--backdrop);
    position: relative;
    font-family: "Arimo", Arial, sans-serif;
  }
  .card {
    position: absolute;
    left: 150px; top: 190px;
    width: 900px; height: 520px;
    background: var(--card-white);
    overflow: hidden;
    box-shadow: 0 6px 18px rgba(0,0,0,.18);
  }
  .top-band {
    position: absolute; left: 0; top: 0; width: 100%; height: 190px;
    background: linear-gradient(100deg, var(--brand-blue) 0%, var(--brand-blue-light) 55%, var(--brand-blue) 100%);
  }
  .rule {
    position: absolute; left: 0; width: 100%; background: var(--brand-blue);
  }
  .rule--thin { top: 198px; height: 5px; }
  .rule--bottom-edge { top: 212px; height: 2px; opacity: .6; }
  .name-tab {
    position: absolute; left: 0; top: 226px; width: 360px; height: 70px;
  }
  .holder {
    position: absolute; left: 34px; top: 232px;
  }
  .holder__name {
    font-family: "Exo 2", sans-serif; font-weight: 800; font-style: italic;
    font-size: 27px; color: var(--brand-blue-deep); text-transform: uppercase;
    letter-spacing: .5px;
  }
  .holder__title { font-size: 20px; color: var(--ink); margin-top: 2px; }
  .contact {
    position: absolute; left: 34px; top: 316px;
    list-style: none; font-size: 20px; letter-spacing: 3px; color: var(--ink);
  }
  .contact li { display: flex; align-items: center; gap: 8px; height: 34px; }
  .contact svg { width: 20px; height: 20px; flex: none; }
  .bottom-band {
    position: absolute; left: 0; top: 392px; width: 470px; height: 66px;
  }
  .company {
    position: absolute; left: 540px; top: 386px;
  }
  .company__brand {
    display: flex; align-items: center; gap: 12px;
    font-family: "Arimo", Arial, sans-serif; font-weight: 700;
    font-size: 52px; line-height: 1; color: var(--brand-blue);
  }
  .company__dot { width: 16px; height: 16px; border-radius: 50%; background: var(--brand-blue); }
  .company__name { font-size: 20px; color: var(--ink); margin-top: 10px; }
  .company__address { font-size: 20px; color: var(--ink); margin-top: 4px; }
</style>
</head>
<body>
  <article class="card">
    <div class="top-band"></div>
    <div class="rule rule--thin"></div>
    <div class="rule rule--bottom-edge"></div>

    <svg class="name-tab" viewBox="0 0 360 70" preserveAspectRatio="none">
      <polygon points="0,0 300,0 360,70 0,70" fill="var(--tab-blue)" opacity=".55"/>
    </svg>

    <div class="holder">
      <p class="holder__name">Dale Whitford</p>
      <p class="holder__title">Manager of Sales and Service</p>
    </div>

    <ul class="contact">
      <li>
        <svg viewBox="0 0 20 20"><rect x="1" y="1" width="18" height="18" rx="3" fill="#2a2a2a"/><rect x="6" y="3.5" width="8" height="13" rx="1.5" fill="#fff"/><rect x="7.5" y="5" width="5" height="8" fill="#2a2a2a"/></svg>
        <span>508-731-2286</span>
      </li>
      <li>
        <svg viewBox="0 0 20 20"><rect x="1" y="1" width="18" height="18" rx="3" fill="#2a2a2a"/><rect x="4" y="6" width="12" height="8" fill="#fff"/><polyline points="4,6 10,11 16,6" fill="none" stroke="#2a2a2a" stroke-width="1.2"/></svg>
        <span>dw71846@mailbrook.net</span>
      </li>
    </ul>

    <svg class="bottom-band" viewBox="0 0 470 66" preserveAspectRatio="none">
      <polygon points="0,0 430,0 470,33 430,66 0,66" fill="var(--brand-blue)"/>
    </svg>

    <div class="company">
      <div class="company__brand"><span class="company__dot"></span>NTS</div>
      <p class="company__name">Northgate Terminal Services, LLC</p>
      <p class="company__address">19 Alder Ln Hollis MA 01842</p>
    </div>
  </article>
</body>
</html>
```